office stationary for pr
pr biz stationery
Creative Brief
Simple
Adaeze Nnorom
14 mabel close eastern lagoonview estate off harmon drive lekki lagos
annorom@pelvora.com
www.pelvora.com
the logo should be used at the back of the business card

```html
<!DOCTYPE html>
<html lang="en">
<head>
<meta charset="utf-8">
<title>Pelvora Designs — Business Cards</title>
<link rel="stylesheet" href="https://fonts.googleapis.com/css2?family=Open+Sans:wght@400&display=swap">
<style>
  :root {
    --canvas: #ffffff;
    --sky: #4fc8f1;
    --sky-mist: #e3f5fd;
    --slate: #808184;
    --ink: #58595b;
    --mark-grey: #7b7b7d;
    --paper: #ffffff;
    --edge: #3a3a3a;
  }
  * { box-sizing: border-box; margin: 0; padding: 0; }
  html, body {
    width: 1200px;
    height: 713px;
    overflow: hidden;
    background: var(--canvas);
    font-family: "Open Sans", Arial, sans-serif;
  }
  .sheet {
    position: relative;
    width: 1200px;
    height: 713px;
  }
  .card {
    position: absolute;
    width: 576px;
    height: 332px;
    overflow: hidden;
  }
  .card--front {
    left: 19px;
    top: 19px;
    background: var(--paper);
    border: 1.5px solid var(--edge);
  }
  .card--back-sky {
    left: 606px;
    top: 19px;
    background: var(--sky);
  }
  .card--back-slate {
    left: 324px;
    top: 366px;
    background: var(--slate);
    border: 1px solid #6d6e70;
  }
  .card--back-sky,
  .card--back-slate {
    display: flex;
    align-items: center;
    justify-content: center;
  }

  .front-watermark {
    position: absolute;
    right: 0;
    top: 0;
    width: 250px;
    height: 100%;
    background: radial-gradient(ellipse 60% 55% at 55% 50%, var(--sky-mist) 0%, rgba(227, 245, 253, 0.6) 55%, rgba(255, 255, 255, 0) 100%);
  }

  .wordmark {
    display: flex;
    align-items: center;
    gap: 10px;
    font-weight: 400;
    letter-spacing: 0.5px;
    white-space: nowrap;
  }
  .wordmark__dot {
    width: 10px;
    height: 10px;
    border-radius: 50%;
    background: currentColor;
  }
  .card--front .wordmark {
    position: absolute;
    left: 30px;
    top: 58px;
    font-size: 28px;
    color: var(--mark-grey);
  }
  .card--back-sky .wordmark {
    font-size: 36px;
    color: var(--mark-grey);
  }
  .card--back-slate .wordmark {
    font-size: 36px;
    color: var(--paper);
  }

  .contact {
    position: absolute;
    left: 30px;
    top: 150px;
    color: var(--ink);
  }
  .contact__name {
    font-size: 20px;
    color: var(--sky);
    margin-bottom: 36px;
  }
  .contact__line {
    font-size: 12.5px;
    line-height: 17px;
  }
  .contact__web {
    color: var(--sky);
  }
</style>
</head>
<body>
  <main class="sheet">
    <section class="card card--front" aria-label="Business card front">
      <div class="front-watermark" role="img" aria-label="Large faint pale-blue brand decoration"></div>
      <div class="wordmark"><span class="wordmark__dot"></span>Pelvora Designs</div>
      <div class="contact">
        <p class="contact__name">Adaeze Nnorom</p>
        <p class="contact__line">14 mabel close, eastern lagoonview estate</p>
        <p class="contact__line">off harmon drive, lekki lagos</p>
        <p class="contact__line">Phone: 08047215530</p>
        <p class="contact__line">Email: annorom@pelvora.com</p>
        <p class="contact__line contact__web">www.pelvora.com</p>
      </div>
    </section>

    <section class="card card--back-sky" aria-label="Business card back, blue">
      <div class="wordmark"><span class="wordmark__dot"></span>Pelvora Designs</div>
    </section>

    <section class="card card--back-slate" aria-label="Business card back, grey">
      <div class="wordmark"><span class="wordmark__dot"></span>Pelvora Designs</div>
    </section>
  </main>
</body>
</html>
```